Non-Profit, Organic, Natural Feel, Clean & Simple Business Cards

Looking for a business card design. Has an organic, natural, new-age, clean and simple look/feel. We are a non-profit group that works with Moringa(a health plant/superfood) by spreading and sharing seeds of Moringa. A design that stands out but clean and professional. I will upload our new logo design. The font can be changed. Also I will upload some pictures of Moringa.
Our Facebook page is www.socialvine.com/TavelliCircle Check us out to get a feel of us.

Target Market(s)

Everyone. Movers & Shakers of The Sustainable, Natural Medicines & Cosmetics, Organic Food Farming Industry. And To The Common Person Or A Local Family.

Industry/Entity Type

Sustainability

Contact Information for Business Card

Email: TavelliSoilCircle@Postvane.com
FB: www.Socialvine.com/TavelliCircle
Website: www.TavelliCircle.com

Requirements
Must have
• Image/Pic/Design of Moringa Leaves. Somewhere on the card. Clean and Clear. So you could easily identify the Moringa from the Business Card. Something Alive, Living, Green Feel to the card design.
Nice to have
• A warm, friendly, professional feel to the design. A organic sustainable concept/future with Moringa is the business card impression/image we are trying to present.

```html
<!DOCTYPE html>
<html lang="en">
<head>
<meta charset="utf-8">
<title>Tavelli Circle – Business Cards</title>
<link href="https://fonts.googleapis.com/css2?family=Cinzel:wght@600&family=Open+Sans:wght@400&display=swap" rel="stylesheet">
<style>
  :root {
    --canvas-bg: #e9e6e0;
    --card-grey: #8f8f84;
    --card-white: #ffffff;
    --brand-green: #5cb531;
    --brand-green-dark: #3f9a22;
    --band-grey: #8d8c84;
    --ink-grey: #7c7c76;
    --text-light: #ffffff;
  }
  * { box-sizing: border-box; margin: 0; padding: 0; }
  html, body {
    width: 1200px; height: 843px; overflow: hidden;
    background: var(--canvas-bg);
  }
  .canvas {
    position: relative; width: 1200px; height: 843px;
  }
  .card {
    position: absolute; left: 280px; width: 640px; height: 366px;
    box-shadow: 0 6px 18px rgba(0,0,0,.18);
    overflow: hidden;
  }
  .card--front { top: 36px; background: var(--card-grey); }
  .card--back  { top: 441px; background: var(--card-white); }

  .brand {
    position: absolute; display: flex; align-items: center; gap: 16px;
  }
  .card--front .brand { left: 50%; top: 50%; transform: translate(-50%, -50%); }
  .card--back .brand  { left: 50%; top: 38px; transform: translateX(-50%); }
  .brand__square {
    width: 44px; height: 44px; background: var(--brand-green);
  }
  .brand__name {
    font-family: "Cinzel", serif; font-weight: 600;
    font-size: 40px; letter-spacing: 3px; line-height: 1;
    white-space: nowrap;
  }
  .card--front .brand__name { color: var(--text-light); }
  .card--back .brand__name  { color: var(--ink-grey); }

  .wave { position: absolute; left: 0; top: 0; width: 640px; height: 366px; }

  .contact {
    position: absolute; left: 44px; top: 190px; color: var(--text-light);
    font-family: "Open Sans", sans-serif;
  }
  .contact__name {
    font-family: "Cinzel", serif; font-weight: 600;
    font-size: 24px; letter-spacing: 1px; line-height: 1.1;
  }
  .contact__role {
    font-family: "Cinzel", serif; font-weight: 600;
    font-size: 16px; letter-spacing: 1px; margin-bottom: 8px;
  }
  .contact__line { font-size: 14px; line-height: 1.45; }
  .contact__social { display: flex; align-items: center; gap: 6px; }
  .contact__social-mark { width: 12px; height: 12px; background: var(--text-light); }
</style>
</head>
<body>
<main class="canvas">
  <section class="card card--front" aria-label="Card front">
    <div class="brand">
      <span class="brand__square"></span>
      <span class="brand__name">TAVELLI CIRCLE</span>
    </div>
  </section>

  <section class="card card--back" aria-label="Card back">
    <div class="brand">
      <span class="brand__square"></span>
      <span class="brand__name">TAVELLI CIRCLE</span>
    </div>
    <svg class="wave" viewBox="0 0 640 366" aria-hidden="true">
      <defs>
        <linearGradient id="greenFill" x1="0" y1="0" x2="0" y2="1">
          <stop offset="0" stop-color="var(--brand-green)"/>
          <stop offset="1" stop-color="var(--brand-green-dark)"/>
        </linearGradient>
      </defs>
      <path d="M0,132 C190,112 380,215 640,238 L640,366 L0,366 Z" fill="var(--band-grey)"/>
      <path d="M0,146 C190,128 380,230 640,254 L640,366 L0,366 Z" fill="url(#greenFill)"/>
    </svg>
    <div class="contact">
      <p class="contact__name">DARA WELLICK</p>
      <p class="contact__role">CEO/FOUNDER</p>
      <p class="contact__line">TavelliSoilCircle@Postvane.com</p>
      <p class="contact__line">www.Socialvine.com/TavelliCircle | www.TavelliCircle.com</p>
      <p class="contact__line contact__social"><span class="contact__social-mark"></span>/TavelliCircle</p>
    </div>
  </section>
</main>
</body>
</html>
```